Simple menu needed for Asian food truck

We are an Asian food truck that attends big festivals. Our menu is very simple featuring only about 5 or 6 dishes, but we need big pictures and lettering to capture the attention of festival goers. Our motto is "Fresh, Authentic, Homemade", it would be great to include that somewhere. We also need a menu that possibly magnetic so that we can easily take off items that are sold out, change pricing or add different dishes for specific venues. Attached is an example of what our current menu looks like.

```html
<!DOCTYPE html>
<html lang="en">
<head>
<meta charset="utf-8">
<title>Golden Wok – Food Truck Menu</title>
<link href="https://fonts.googleapis.com/css2?family=Oswald:wght@400;500;600;700&display=swap" rel="stylesheet">
<style>
  :root {
    --board: #1b1a19;
    --board-light: #2c2a28;
    --gold: #e3a530;
    --tan: #d9c9a3;
    --white: #f7f4ee;
    --muted: #cfc8bb;
    --frame: #3a352c;
    --page: #ffffff;
  }
  * { box-sizing: border-box; margin: 0; padding: 0; }
  html, body { width: 1200px; height: 2672px; overflow: hidden; background: var(--page); }
  body { position: relative; font-family: "Oswald", sans-serif; color: var(--white); }

  .board {
    position: absolute; left: 48px; top: 56px; width: 1104px; height: 1992px;
    border-radius: 28px; border: 4px solid var(--frame);
    background: radial-gradient(ellipse at 50% 40%, var(--board-light), var(--board) 75%);
  }
  .magnet {
    position: absolute; left: 120px; width: 968px; height: 240px;
    border-radius: 18px; border: 4px solid var(--frame);
    background: radial-gradient(ellipse at 50% 50%, var(--board-light), var(--board) 80%);
  }
  .magnet--teriyaki { top: 2088px; }
  .magnet--pho { top: 2360px; }

  .masthead { position: absolute; left: 20px; top: 36px; display: flex; align-items: center; height: 160px; white-space: nowrap; }
  .masthead__menu { font-size: 150px; font-weight: 600; color: var(--tan); line-height: 1; }
  .masthead__rule { width: 5px; height: 136px; background: var(--gold); margin: 0 18px; }
  .masthead__fresh { font-size: 150px; font-weight: 700; color: var(--gold); line-height: 1; }
  .masthead__motto { margin-left: 14px; display: flex; flex-direction: column; color: var(--gold); font-weight: 600; font-size: 52px; line-height: 0.98; }

  .photo {
    position: absolute; left: 108px; width: 216px; height: 216px; border-radius: 50%;
    border: 6px solid var(--white);
  }
  .photo--egg { top: 240px; background: radial-gradient(circle at 45% 45%, #e6b45a, #b3702a 70%, #f2efe6); }
  .photo--spring { top: 496px; background: radial-gradient(circle at 50% 50%, #f0c4b0, #8fb07a 70%, #f4f1ea); }
  .photo--bbq { top: 752px; background: radial-gradient(circle at 50% 50%, #8a3a20, #4a1c12 70%, #2a1a12); }
  .photo--rice { top: 1028px; background: radial-gradient(circle at 50% 50%, #d9c08a, #a8864e 70%, #f3efe6); }
  .photo--wing { top: 1284px; background: radial-gradient(circle at 50% 50%, #e4a54c, #a0602a 70%, #3b3631); }
  .photo--tea { top: 1548px; background: linear-gradient(90deg, #f08a6a, #f7c24a 50%, #f4a03c); }
  .photo--teriyaki { left: 8px; top: 16px; width: 200px; height: 200px; background: radial-gradient(circle at 50% 50%, #d9a050, #8a5320 70%, #3a2c22); }
  .photo--pho { left: 8px; top: 16px; width: 200px; height: 200px; background: radial-gradient(circle at 50% 50%, #8a6a3c, #5a7a48 60%, #2c2a28); }

  .item { position: absolute; left: 384px; width: 640px; }
  .magnet .item { left: 312px; width: 636px; }
  .item__title { font-size: 70px; font-weight: 600; line-height: 1; color: var(--white); white-space: nowrap; }
  .item__title--accent { color: var(--tan); font-size: 84px; }
  .line { display: flex; align-items: baseline; font-size: 30px; font-weight: 500; color: var(--muted); white-space: nowrap; line-height: 1.15; }
  .line__dots { flex: 1; min-width: 0; overflow: hidden; margin: 0 8px; letter-spacing: 6px; }
  .line__dots::before { content: ". . . . . . . . . . . . . . . . . . . . . . . . . . . . . . . . . . . . . . . . . ."; }
  .line__qty { font-size: 36px; color: var(--white); margin-right: 10px; }
  .price { color: var(--gold); font-weight: 600; font-size: 70px; line-height: 1; }
  .price--small { font-size: 54px; }
  .title-row { display: flex; align-items: flex-end; justify-content: space-between; }
  .tag { color: var(--gold); font-size: 40px; font-weight: 600; }

  .egg { top: 274px; }
  .spring { top: 534px; }
  .bbq { top: 774px; }
  .rice { top: 1078px; }
  .wing { top: 1314px; }
  .tea { top: 1590px; }
  .teriyaki { top: 62px; }
  .pho { top: 78px; }

  .brand { position: absolute; left: 0; width: 1096px; top: 1776px; display: flex; flex-direction: column; align-items: center; }
  .brand__mark { display: flex; align-items: center; gap: 14px; }
  .brand__dot { width: 40px; height: 40px; border-radius: 50%; border: 4px solid var(--gold); }
  .brand__name { font-size: 46px; font-weight: 600; color: var(--gold); letter-spacing: 3px; line-height: 1.1; }
  .payments { margin-top: 30px; display: flex; flex-direction: column; align-items: center; gap: 10px; }
  .payments__name { font-size: 28px; color: var(--white); font-weight: 500; line-height: 1; }
  .payments__cards { display: flex; gap: 8px; }
  .payments__cards span { width: 40px; height: 26px; border-radius: 4px; background: var(--muted); }
</style>
</head>
<body>
  <section class="board">
    <header class="masthead">
      <span class="masthead__menu">MENU</span>
      <span class="masthead__rule"></span>
      <span class="masthead__fresh">FRESH</span>
      <span class="masthead__motto"><span>AUTHENTIC</span><span>HOMEMADE</span></span>
    </header>

    <div class="photo photo--egg" role="img" aria-label="Photo of crispy egg rolls"></div>
    <div class="item egg">
      <div class="item__title">EGG ROLLS</div>
      <div class="line"><span>( CHICKEN OR PORK )</span><span class="line__dots"></span><span class="line__qty">3 FOR</span><span class="price">$6.50</span></div>
      <div class="line"><span>“ADD” SIDE OF FRIED RICE</span><span class="line__dots"></span><span class="price price--small">$4</span></div>
    </div>

    <div class="photo photo--spring" role="img" aria-label="Photo of fresh spring rolls"></div>
    <div class="item spring">
      <div class="item__title">FRESH SPRING ROLLS</div>
      <div class="line"><span>( SHRIMP OR VEGGIE )</span><span class="line__dots"></span><span class="line__qty">2 FOR</span><span class="price">$6.50</span></div>
    </div>

    <div class="photo photo--bbq" role="img" aria-label="Photo of Chinese BBQ pork skewers"></div>
    <div class="item bbq">
      <div class="item__title">CHINESE BBQ PORK</div>
      <div class="line"><span class="item__title item__title--accent">SKEWERS</span><span class="line__dots"></span><span class="line__qty">2 FOR</span><span class="price">$6.50</span></div>
      <div class="line"><span>“ADD” SIDE OF FRIED RICE</span><span class="line__dots"></span><span class="price price--small">$4</span></div>
    </div>

    <div class="photo photo--rice" role="img" aria-label="Photo of a bowl of fried rice"></div>
    <div class="item rice">
      <div class="title-row"><span class="item__title">FRIED RICE</span><span class="price price--small">$5.50</span></div>
      <div class="line"><span>( CHICKEN OR PORK )</span><span class="line__dots"></span><span class="tag">BOWL</span></div>
    </div>

    <div class="photo photo--wing" role="img" aria-label="Photo of stuffed chicken wings"></div>
    <div class="item wing">
      <div class="title-row"><span class="item__title">ANGEL WING</span><span class="price price--small">$9</span></div>
      <div class="line"><span>( STUFFED CHICKEN WING )</span></div>
      <div class="line"><span>WITH SIDE OF FRIED RICE</span><span class="line__dots"></span><span class="tag">COMBO</span></div>
    </div>

    <div class="photo photo--tea" role="img" aria-label="Photo of glasses of flavored iced tea"></div>
    <div class="item tea">
      <div class="item__title">FLAVORED TEA</div>
      <div class="line"><span>STRAWBERRY, MANGO, OR PEACH</span><span class="line__dots"></span><span class="price price--small">$5</span></div>
    </div>

    <footer class="brand">
      <div class="brand__mark"><span class="brand__dot"></span><span class="brand__name">GOLDEN WOK</span></div>
      <div class="payments">
        <span class="payments__name">Tapay</span>
        <div class="payments__cards"><span></span><span></span><span></span><span></span></div>
      </div>
    </footer>
  </section>

  <section class="magnet magnet--teriyaki">
    <div class="photo photo--teriyaki" role="img" aria-label="Photo of chicken teriyaki"></div>
    <div class="item teriyaki">
      <div class="item__title">CHICKEN TERIYAKI</div>
      <div class="line"><span>WITH SIDE OF STEAM RICE</span><span class="line__dots"></span><span class="price price--small">$10.50</span></div>
    </div>
  </section>

  <section class="magnet magnet--pho">
    <div class="photo photo--pho" role="img" aria-label="Photo of a bowl of beef pho"></div>
    <div class="item pho">
      <div class="line"><span class="item__title">BEEF PHO</span><span class="line__dots"></span><span class="price price--small">$10.50</span></div>
    </div>
  </section>
</body>
</html>
```